Tovimerra: Travel business card redesign

We need a clean elegant look for our cards featuring blue and orange. Look should communicate a sense of strong design and seem uncluttered. The company is Tovimerra which means escape to bliss. As in every trip is an escape to bliss. Feel free to reinvent the logo or just tweak it. Colors should be blue like Caribbean waters and a saturated orange. Keep it clean and simple.
Please match the information in the sample uploaded but the sample is horrible -- a non-starter -- use for information only. also please add managing director to my name as title

Target Market(s)
potential clients, hotels, trade publications
Industry/Entity Type
Travel Industry
Contact Information for Business Card
as above
Requirements
Must have
- Font should be century gothic. Colors below are close but a but prefer lighter in each case.

```html
<!DOCTYPE html>
<html lang="en">
<head>
<meta charset="utf-8">
<title>Tovimerra business cards</title>
<link href="https://fonts.googleapis.com/css2?family=Mulish:wght@400;600;800&display=swap" rel="stylesheet">
<style>
  :root {
    --bg: #e9e6e1;
    --card-white: #ffffff;
    --card-dark: #2a2a2a;
    --orange: #f0892b;
    --blue: #5fafd6;
    --ink: #1f1f1f;
  }
  * { margin: 0; padding: 0; box-sizing: border-box; }
  html, body { width: 1200px; height: 900px; overflow: hidden; }
  body {
    background: var(--bg);
    font-family: "Mulish", "Century Gothic", sans-serif;
    position: relative;
  }
  .card {
    position: absolute;
    width: 560px;
    height: 320px;
    box-shadow: 0 6px 18px rgba(0,0,0,0.18);
    overflow: hidden;
  }

  /* Back side */
  .card-back {
    left: 560px; top: 90px;
    background: var(--card-dark);
    color: var(--card-white);
  }
  .card-back .wordmark {
    position: absolute;
    left: 0; right: 0; top: 92px;
    text-align: center;
    font-weight: 800;
    font-size: 64px;
    letter-spacing: -1px;
    color: var(--card-white);
  }
  .card-back .tagline-row {
    position: absolute;
    left: 28px; right: 28px; top: 200px;
    display: flex; align-items: center; gap: 14px;
  }
  .card-back .tagline-row .line {
    flex: 1; height: 1px; background: var(--card-white); opacity: 0.85;
  }
  .card-back .tagline {
    font-weight: 600; font-size: 17px; letter-spacing: 1.2px; white-space: nowrap;
  }

  /* Front side */
  .card-front {
    left: 90px; top: 480px;
    background: var(--card-white);
    color: var(--ink);
  }
  .card-front .bands { position: absolute; inset: 0; }
  .card-front .person {
    position: absolute; left: 40px; top: 24px;
  }
  .person .name { font-weight: 800; font-size: 18px; line-height: 1.1; }
  .person .first { color: var(--orange); }
  .person .last { color: var(--blue); }
  .person .title { font-size: 13px; margin-top: 3px; }
  .card-front .address {
    position: absolute; left: 40px; top: 100px;
    font-size: 14px; line-height: 1.35; font-style: normal;
  }
  .card-front .contacts {
    position: absolute; left: 22px; top: 152px;
    list-style: none; font-size: 14px; line-height: 1.45;
  }
  .contacts li { display: flex; align-items: center; gap: 8px; }
  .contacts svg { width: 11px; height: 11px; flex: none; }
  .card-front .wordmark {
    position: absolute; left: 290px; top: 118px;
    font-weight: 800; font-size: 50px; letter-spacing: -1px;
    color: var(--orange);
  }
</style>
</head>
<body>

  <section class="card card-back" aria-label="Card back">
    <div class="wordmark">Tovimerra</div>
    <div class="tagline-row">
      <span class="line"></span>
      <span class="tagline">JOURNEYS MADE WITH CARE</span>
      <span class="line"></span>
    </div>
  </section>

  <section class="card card-front" aria-label="Card front">
    <svg class="bands" width="560" height="320" viewBox="0 0 560 320">
      <polygon points="0,250 300,250 290,276 0,276" fill="var(--blue)"/>
      <polygon points="302,278 560,278 560,320 286,320" fill="var(--orange)"/>
    </svg>

    <div class="person">
      <div class="name"><span class="first">Reid</span> <span class="last">Calloway</span></div>
      <div class="title">Managing Director</div>
    </div>

    <address class="address">
      4417 Marlow Vista Lane N,<br>Harbor Vale, 71236
    </address>

    <ul class="contacts">
      <li>
        <svg viewBox="0 0 12 12"><path d="M2 1 L4.5 1 L5 4 L3.6 5 Q4.8 7.4 7 8.4 L8 7 L11 7.5 L11 10 Q5 11 1.5 3 Z" fill="var(--orange)"/></svg>
        877.86.TOVI(8684)
      </li>
      <li>
        <svg viewBox="0 0 12 12"><rect x="2" y="1" width="8" height="10" rx="1.2" fill="none" stroke="var(--orange)" stroke-width="1.6"/></svg>
        323.555.0142
      </li>
      <li>
        <svg viewBox="0 0 12 12"><rect x="1.5" y="2" width="9" height="9" rx="1" fill="var(--orange)"/><rect x="3.5" y="4" width="5" height="2" fill="#fff"/></svg>
        310.555.0187
      </li>
      <li>
        <svg viewBox="0 0 12 12"><circle cx="6" cy="6" r="5" fill="var(--orange)"/><path d="M1 6 H11 M6 1 Q3 6 6 11 Q9 6 6 1" fill="none" stroke="#fff" stroke-width="0.9"/></svg>
        www.tovimerra.com
      </li>
    </ul>

    <div class="wordmark">Tovimerra</div>
  </section>

</body>
</html>
```